Crest Automotive Reconditioning Business Card

We need a professional business card that features our logo, a picture of the employee, and a brief list of our services.
I've attached a logo, and will attach photos at a later date.
The four services that need to be listed are Bumper repair and repainting, road rash repair, clear coat scratch repair, and automotive touch-up.
Target Market(s)
30 - 40 year male general managers of automobile dealerships. They are used to seeing every vendor gimmick under the sun. This brochure needs to impress with its simplicity and honesty.
Industry/Entity Type
Automotive
Look and feel
Each slider illustrates characteristics of the customer's brand and the style your logo design should communicate.

```html
<!DOCTYPE html>
<html lang="en">
<head>
<meta charset="utf-8">
<title>Crest Automotive Reconditioning – Business Card</title>
<link href="https://fonts.googleapis.com/css2?family=Open+Sans:wght@300;400;700;800&display=swap" rel="stylesheet">
<style>
  :root {
    --page-bg: #e9e9e9;
    --card-white: #ffffff;
    --card-grey: #dcdcdc;
    --brand-red: #d4070f;
    --brand-red-dark: #8e0006;
    --ink: #2a2a2a;
    --card-black: #050505;
    --card-charcoal: #2a2a2a;
    --text-light: #ffffff;
    --text-soft: #e6e6e6;
  }
  * { box-sizing: border-box; margin: 0; padding: 0; }
  html, body { width: 1200px; height: 1000px; overflow: hidden; }
  body {
    background: var(--page-bg);
    font-family: "Open Sans", Arial, sans-serif;
    position: relative;
  }
  .card {
    position: absolute;
    left: 250px;
    width: 700px;
    height: 400px;
    border-radius: 26px;
    overflow: hidden;
    box-shadow: 0 8px 24px rgba(0,0,0,0.18);
  }

  /* Front */
  .card-front {
    top: 50px;
    background: radial-gradient(ellipse at 50% 40%, var(--card-white) 30%, var(--card-grey) 100%);
  }
  .brand-name {
    position: absolute;
    left: 0; right: 0; top: 110px;
    text-align: center;
    color: var(--ink);
    font-weight: 800;
    text-transform: uppercase;
    line-height: 1;
  }
  .brand-name .brand-main { display: block; font-size: 76px; letter-spacing: 2px; }
  .brand-name .brand-sub { display: block; font-size: 20px; letter-spacing: 1.5px; margin-top: 8px; }
  .front-band {
    position: absolute;
    left: 0; right: 0; bottom: 0;
    height: 58px;
    background: linear-gradient(180deg, var(--brand-red) 0%, var(--brand-red-dark) 100%);
    color: var(--text-light);
    font-size: 17px;
    display: flex; align-items: center; justify-content: center;
    letter-spacing: 0.5px;
  }

  /* Back */
  .card-back {
    top: 510px;
    background: radial-gradient(ellipse at 60% 35%, var(--card-charcoal) 0%, var(--card-black) 75%);
  }
  .flag-area {
    position: absolute;
    left: 0; top: 60px;
    width: 340px; height: 240px;
    background: linear-gradient(160deg, var(--brand-red) 0%, #9b0008 45%, #3a0003 100%);
    clip-path: polygon(60% 0, 100% 0, 100% 45%, 30% 100%, 0 100%, 0 60%);
    opacity: 0.95;
  }
  .vehicles-area {
    position: absolute;
    left: 260px; top: 150px;
    width: 440px; height: 190px;
    background: radial-gradient(ellipse at 50% 55%, #1c1c1c 0%, rgba(10,10,10,0) 70%);
  }
  .services {
    position: absolute;
    left: 362px; top: 44px;
    list-style: none;
    color: var(--text-soft);
    font-size: 17px;
    text-transform: uppercase;
    line-height: 33px;
  }
  .person {
    position: absolute;
    right: 270px; top: 276px;
    text-align: right;
    color: var(--text-light);
    text-transform: uppercase;
  }
  .person-name { font-size: 30px; font-weight: 800; line-height: 38px; }
  .person-title { font-size: 30px; font-weight: 300; line-height: 38px; }
  .divider {
    position: absolute;
    left: 446px; top: 208px;
    width: 1.5px; height: 82px;
    background: var(--text-soft);
  }
  .contacts {
    position: absolute;
    left: 462px; top: 212px;
    list-style: none;
    color: var(--text-light);
    font-size: 17px;
  }
  .contacts li { display: flex; align-items: center; height: 36px; }
  .contact-icon { width: 24px; height: 24px; margin-right: 10px; flex: none; }
</style>
</head>
<body>

  <section class="card card-front" aria-label="Card front">
    <h1 class="brand-name">
      <span class="brand-main">Crest</span>
      <span class="brand-sub">Automotive Reconditioning</span>
    </h1>
    <div class="front-band">www.yourwebsite.com</div>
  </section>

  <section class="card card-back" aria-label="Card back">
    <div class="flag-area" role="img" aria-label="Red and black chequered flag graphic"></div>
    <div class="vehicles-area" role="img" aria-label="Faint dark photographs of cars"></div>

    <ul class="services">
      <li>Bumper repair and repainting</li>
      <li>Clear coat scratch repair</li>
      <li>and automotive touch-up.</li>
      <li>Road rash repair</li>
    </ul>

    <div class="person">
      <p class="person-name">Your Name Here</p>
      <p class="person-title">Your Title</p>
    </div>

    <div class="divider"></div>

    <ul class="contacts">
      <li>
        <svg class="contact-icon" viewBox="0 0 24 24" aria-hidden="true">
          <circle cx="12" cy="12" r="12" fill="var(--brand-red)"/>
          <rect x="8.5" y="5.5" width="7" height="13" rx="1.2" fill="none" stroke="#fff" stroke-width="1.4"/>
          <circle cx="12" cy="16" r="0.9" fill="#fff"/>
        </svg>
        (+61) 04 5550 1827
      </li>
      <li>
        <svg class="contact-icon" viewBox="0 0 24 24" aria-hidden="true">
          <circle cx="12" cy="12" r="12" fill="var(--brand-red)"/>
          <rect x="6" y="8" width="12" height="8.5" fill="none" stroke="#fff" stroke-width="1.4"/>
          <path d="M6 8 L12 13 L18 8" fill="none" stroke="#fff" stroke-width="1.4"/>
        </svg>
        sales@crestrecon.com.au
      </li>
    </ul>
  </section>

</body>
</html>
```